Investment Fund Investor newsletter

I deleted the tear sheet example which was provided for design purposes only and not for content. Please see the simple outline for the newsletter and the related sections.

Please be clear this project is for a newsletter template. This means a template that can be updated on a monthly or quarterly basis with new content for our audience. Sections should include: Operations Update, Financial Update, Energy Investor News.

We need a template for a newsletter that can be sent out in Word format and also able to send out via Mailchimp. Audience are current investors in our oil and gas fund. These investors are high net worth individuals and private equity firms so the branding needs to be high end, sophisticated and corporate. Please see website and attached tear sheet for the type of branding that we want to match. Website is www.quarrybell-power.com
Please see website and tear sheet for the color scheme that we want.

Target Market(s)

Our current fund investors that include high net worth investors and CEOs of private equity companies

Industry/Entity Type

oil and gas... investment

Font styles to use
Serif

Requirements
Must have
• Word file and can send via Mailchimp too

```html
<!DOCTYPE html>
<html lang="en">
<head>
<meta charset="utf-8">
<title>Quarrybell Power Partners – Investor Newsletter</title>
<link rel="stylesheet" href="https://fonts.googleapis.com/css2?family=Playfair+Display:wght@400;700&family=Roboto:wght@400;500;700&display=swap">
<style>
:root{
  --teal:#0f8fb3;
  --navy:#1b2a4a;
  --ink:#1d1d1f;
  --text:#2c2c2c;
  --tile:#dcdcdc;
  --tile-text:#6d6d6d;
  --rule:#b9cfdc;
  --white:#ffffff;
  --serif:'Playfair Display', Georgia, serif;
  --sans:'Roboto', Arial, sans-serif;
}
*{margin:0;padding:0;box-sizing:border-box}
html,body{width:1200px;height:4352px;overflow:hidden}
body{position:relative;font-family:var(--sans);color:var(--text);font-variant-numeric:lining-nums}
.backdrop{position:absolute;inset:0;background:linear-gradient(180deg,#6fb8d9 0%,#a9d6ec 25%,#cfe6f1 50%,#9cc7dd 75%,#5f8fae 100%)}
.sheet{position:absolute;left:69px;top:106px;width:1060px;height:4131px;background:linear-gradient(180deg,rgba(220,235,244,.96),rgba(230,240,246,.92) 60%,rgba(220,235,244,.9))}
.abs{position:absolute}

.phone{left:106px;top:206px;font-size:30px;color:var(--ink);display:flex;align-items:center;gap:18px;font-family:var(--serif);font-weight:400}
.phone svg{width:30px;height:30px}
.brand{left:400px;top:258px;width:400px;text-align:center;font-family:var(--serif);color:var(--ink)}
.brand .name{font-size:34px;letter-spacing:5px;display:block;font-weight:400}
.brand .sub{font-size:14px;letter-spacing:8px;display:block;margin-top:0}
.social{top:203px;display:flex;gap:22px}
.social span{width:50px;height:50px;border-radius:50%;background:var(--ink);display:block}

.hero-photo{left:106px;top:343px;width:606px;height:639px;background:linear-gradient(180deg,#2a3350 0%,#c25a1c 55%,#f2a120 72%,#2a1a10 100%)}
.hero-text{left:712px;top:343px;width:380px;height:639px;background:var(--teal);display:flex;flex-direction:column;align-items:center;justify-content:center;text-align:center;color:var(--white);padding:0 24px}
.hero-text .eyebrow{font-family:var(--sans);font-weight:500;font-size:18px;letter-spacing:3px;border-bottom:2px solid var(--white);padding-bottom:12px;margin-bottom:26px}
.hero-text .headline{font-family:var(--serif);font-weight:700;font-size:36px;line-height:49px}

.stat{top:1051px;width:330px;text-align:center;font-size:21px;line-height:31px;color:var(--ink)}
.stat .icon{height:180px;margin:0 auto 20px;background:linear-gradient(180deg,#3a3a3a,#111);opacity:.85}
.stat.big{font-size:29px;line-height:32px;font-weight:500}

.ops{left:106px;top:1460px;width:986px;height:399px;background:linear-gradient(135deg,#05111f,#0b2a3a 60%,#06121f);text-align:center;color:var(--white)}
.ops h2{font-family:var(--serif);font-size:35px;margin-top:50px}
.ops p{font-size:20.5px;font-weight:700;line-height:31px;width:820px;margin:20px auto 0}
.btn{display:inline-block;margin-top:40px;width:268px;height:55px;border:3px solid var(--white);font-size:21px;font-weight:500;line-height:49px}

.tile{background:var(--tile);display:flex;align-items:center;justify-content:center;font-family:var(--serif);font-weight:700;color:var(--tile-text);font-size:30px;text-align:center}

.section-title{left:200px;width:800px;text-align:center;font-family:var(--serif);font-weight:700;font-size:35px;line-height:50px;color:var(--ink)}
.section-bar{left:400px;width:400px;height:8px;border-radius:4px;background:var(--teal)}

.figures{left:160px;top:2290px;width:880px;border-collapse:collapse;font-size:24px}
.figures td{height:54px;border-bottom:2px solid var(--rule);padding:0 10px}
.figures td.value{text-align:right;font-family:var(--serif);font-weight:700;color:var(--teal);font-size:26px}

.spine{left:597px;top:2710px;width:6px;height:260px;background:var(--teal)}
.step{left:552px;width:96px;height:96px;border-radius:50%;background:var(--teal);color:var(--white);font-family:var(--serif);font-weight:700;font-size:44px;display:flex;align-items:center;justify-content:center}
.step-text{font-size:24.5px;line-height:36px;color:var(--text);width:430px}
.step-text b{font-weight:700;color:var(--ink)}
.step-text.left{left:84px;text-align:right}
.step-text.right{left:693px}

.navy{left:69px;top:3516px;width:1060px;height:721px;background:linear-gradient(180deg,#1d2c4c,#16223d 60%,#233457)}
.team{left:106px;top:3121px;width:986px;height:505px;background:var(--teal)}
.team h2{position:absolute;left:0;top:64px;width:100%;text-align:center;font-family:var(--serif);font-size:35px;color:var(--white)}
.member{top:3278px;width:235px;text-align:center;color:var(--white)}
.member .portrait{width:210px;height:238px;margin:0 auto;background:linear-gradient(180deg,#9a9a9a,#4a4a4a);clip-path:polygon(50% 0,100% 25%,100% 75%,50% 100%,0 75%,0 25%)}
.member .n{font-size:25px;font-weight:500;margin-top:24px}
.member .r{font-size:20px;font-weight:500;margin-top:10px}

.foot-brand{left:400px;top:3890px;width:400px;text-align:center;font-family:var(--serif);color:var(--white)}
.foot-brand .name{font-size:40px;letter-spacing:7px;display:block}
.foot-brand .sub{font-size:16px;letter-spacing:10px;display:block}
.contact{left:200px;width:800px;text-align:center;color:var(--white);font-size:30px}
</style>
</head>
<body>
<div class="backdrop" role="img" aria-label="Sky and sea with offshore oil platform"></div>
<div class="sheet"></div>

<div class="abs phone">
  <svg viewBox="0 0 24 24" aria-hidden="true"><path fill="#1d1d1f" d="M6.6 10.8a15.1 15.1 0 0 0 6.6 6.6l2.2-2.2c.3-.3.7-.4 1-.2 1.1.4 2.3.6 3.6.6.6 0 1 .4 1 1V20c0 .6-.4 1-1 1A17 17 0 0 1 3 4c0-.6.4-1 1-1h3.5c.6 0 1 .4 1 1 0 1.3.2 2.5.6 3.6.1.3 0 .7-.2 1l-2.3 2.2z"/></svg>
  (432) 555-0187
</div>
<div class="abs brand"><span class="name">QUARRYBELL</span><span class="sub">POWER PARTNERS</span></div>
<div class="abs social" style="left:897px" aria-label="Social links"><span></span><span></span><span></span></div>

<div class="abs hero-photo" role="img" aria-label="Pumpjack silhouetted against an orange sunset"></div>
<div class="abs hero-text">
  <div class="eyebrow">INVESTOR NEWSLETTER</div>
  <div class="headline">CONSOLIDATING WEST TEXAS CONVENTIONAL OIL &amp; GAS ASSETS INTO A HIGH RETURN FUND.</div>
</div>

<div class="abs stat" style="left:87px"><div class="icon" role="img" aria-label="100 years anniversary badge" style="width:180px;border-radius:50%"></div>100+ years combined experience evaluating and operating conventional oil and gas wells in West Texas</div>
<div class="abs stat" style="left:435px"><div class="icon" role="img" aria-label="Coins and money bag icon" style="width:170px;border-radius:30px"></div>1000+ Targeted conventional oil &amp; gas assets with $250MM+ enterprise value goal</div>
<div class="abs stat big" style="left:783px"><div class="icon" role="img" aria-label="Map of Texas and the Permian Basin" style="width:170px;margin-bottom:10px"></div>Focused<br>on<br>Permian Basin</div>

<section class="abs ops">
  <h2>OPERATIONS UPDATE</h2>
  <p>This period our operator, Halvren Resources, completed workovers and returned wells to production across our Permian Basin leases. Summarise field activity, production uplift, new wells brought online and safety record here each edition.</p>
  <span class="btn">Read Full Update</span>
</section>

<div class="abs tile" style="left:106px;top:1869px;width:339px;height:133px">Marrow Quill</div>
<div class="abs tile" style="left:452px;top:1869px;width:304px;height:133px;font-size:24px">Brenley Oakes &amp; Tull</div>
<div class="abs tile" style="left:763px;top:1869px;width:329px;height:133px">Ridgeline Bank</div>
<div class="abs tile" style="left:106px;top:2009px;width:339px;height:133px">Cinderhill Oil</div>
<div class="abs tile" style="left:452px;top:2009px;width:304px;height:133px;font-size:36px">Vantor Works</div>
<div class="abs tile" style="left:763px;top:2009px;width:329px;height:133px">Ridgeline Bank</div>

<section>
  <h2 class="abs section-title" style="top:2200px">FINANCIAL UPDATE</h2>
  <div class="abs section-bar" style="top:2254px"></div>
  <table class="abs figures">
    <tr><td>Net production this quarter (BOE/day)</td><td class="value">0,000</td></tr>
    <tr><td>Gross revenue</td><td class="value">$0.0MM</td></tr>
    <tr><td>Distributions paid to investors</td><td class="value">$0.0MM</td></tr>
    <tr><td>Assets acquired to date</td><td class="value">00</td></tr>
  </table>
</section>

<section>
  <h2 class="abs section-title" style="top:2560px">ENERGY INVESTOR NEWS</h2>
  <div class="abs section-bar" style="top:2614px"></div>
  <div class="abs spine"></div>
  <div class="abs step" style="top:2660px">01</div>
  <div class="abs step" style="top:2790px">02</div>
  <div class="abs step" style="top:2920px">03</div>
  <div class="abs step-text left" style="top:2663px"><b>Permian output</b><br>Summary of this period's basin production and pricing news.</div>
  <div class="abs step-text right" style="top:2793px"><b>Market outlook</b><br>Key points on oil and gas prices and what they mean for the fund.</div>
  <div class="abs step-text left" style="top:2923px"><b>Policy &amp; regulation</b><br>Brief on Texas rules and federal news affecting producers.</div>
</section>

<div class="abs navy" role="img" aria-label="Dark blue pumpjack scene at dusk"></div>
<section class="abs team"><h2>THE TEAM</h2></section>
<div class="abs member" style="left:114px"><div class="portrait" role="img" aria-label="Portrait of Dale Whitcomb"></div><div class="n">Dale Whitcomb</div><div class="r">Managing Partner</div></div>
<div class="abs member" style="left:358px"><div class="portrait" role="img" aria-label="Portrait of Neil Ashford"></div><div class="n">Neil Ashford</div><div class="r">Partner</div></div>
<div class="abs member" style="left:602px"><div class="portrait" role="img" aria-label="Portrait of Laura Whitcomb"></div><div class="n">Laura Whitcomb</div><div class="r">Managing Partner</div></div>
<div class="abs member" style="left:846px"><div class="portrait" role="img" aria-label="Portrait of Frank Medina"></div><div class="n">Frank Medina</div><div class="r">Operations Manager</div></div>

<div class="abs foot-brand"><span class="name">QUARRYBELL</span><span class="sub">POWER PARTNERS</span></div>
<div class="abs contact" style="top:3975px">PH: (432) 555-0187</div>
<div class="abs contact" style="top:4025px">EM: info@quarrybell-power.com</div>
<div class="abs social" style="left:502px;top:4094px" aria-label="Social links"><span style="background:#fff"></span><span style="background:#fff"></span><span style="background:#fff"></span></div>
</body>
</html>
```